Landing Page Design für Tor- und Zaunbaufirma
Zielgruppe
der Kunde ist eine Tor- und Zaunbaufirma. Die Zielgruppen sind private Häuslebauer und Firmen.
Aufgabenstellung
Die Farben des Logos sollen nur sehr sparsam eingesetzt werden.
Die Navigation soll sich an der jetzigen Webseite orientieren. www.frenk-gitterwerk.de
Impressum und Datenschutz dezenter platzieren
Kommunikationsdaten vordergründig darstellen
mehr als 25-Jahre Erfahrung im Tor- und Zaunbau
Regionalität beachten

```html
<!DOCTYPE html>
<html lang="de">
<head>
<meta charset="utf-8">
<title>Tor &amp; Zaunbau Frenk</title>
<link href="https://fonts.googleapis.com/css2?family=Montserrat:wght@400;500;600;700;800&display=swap" rel="stylesheet">
<style>
:root{
  --ink:#2a2a2a;
  --text:#444;
  --muted:#777;
  --accent:#e6007e;
  --soft:#f3f3f3;
  --row:#ebebeb;
  --footer:#2b2b2b;
  --wood:#a85a25;
}
*{margin:0;padding:0;box-sizing:border-box}
html,body{width:1200px;height:3661px;overflow:hidden}
body{font-family:'Montserrat',sans-serif;color:var(--text);background:#fff;position:relative}
.abs{position:absolute}
.photo{position:absolute}
.topbar{top:0;left:0;width:1200px;height:34px;background:var(--soft);font-size:11px;color:var(--muted)}
.topbar span{position:absolute;top:11px;display:flex;align-items:center;gap:8px}
.header{top:34px;left:0;width:1200px;height:82px}
.brand{position:absolute;left:67px;top:31px;font-weight:800;font-size:22px;color:var(--ink);display:flex;align-items:center;gap:10px}
.brand i{display:block;width:18px;height:18px;background:var(--accent)}
.nav{position:absolute;top:32px;font-size:13px;color:var(--text)}
.hero-card{left:496px;top:291px;width:637px;height:161px;background:#fff;padding:24px 30px}
.hero-card h1{font-size:29px;font-weight:700;line-height:40px;color:var(--ink)}
.hero-card p{font-size:15.5px;margin-top:14px;margin-left:4px}
.watermark{font-weight:800;color:#f1f1f1;letter-spacing:4px}
h2{font-weight:400;font-size:30px;color:var(--ink)}
h2 b{font-weight:700}
.intro h2{font-size:28px;font-weight:700}
.small{font-size:11.5px;line-height:24px}
.strengths li{list-style:none;display:flex;align-items:center;gap:30px;font-size:12.5px;height:46px}
.services{top:1530px;left:0;width:1200px;height:678px;background:var(--soft)}
.card-label{font-size:12.5px;font-weight:700;color:var(--ink);display:flex;align-items:center;justify-content:center;gap:14px;text-align:center}
.profile{left:589px;top:2349px;width:544px}
.profile .row{height:71.6px;display:flex;align-items:center;padding-left:22px;gap:30px;font-size:12.5px;line-height:24px}
.profile .row:nth-child(odd){background:var(--row)}
.profile .row:nth-child(even){background:var(--soft)}
.profile b{color:var(--ink)}
.footer{top:3341px;left:0;width:1200px;height:320px;background:var(--footer);color:#fff}
.footer h4{font-size:12.5px;font-weight:700;position:absolute;top:51px}
.footer ul{list-style:none;position:absolute;top:79px;font-size:12.5px;line-height:24px}
a{color:inherit}
</style>
</head>
<body>

<div class="abs topbar">
  <span style="left:67px"><svg width="9" height="13" viewBox="0 0 9 13"><rect x="1" y="0.5" width="7" height="12" rx="1" fill="none" stroke="#777"/></svg>0172 / 000 12 34</span>
  <span style="left:545px"><svg width="13" height="13" viewBox="0 0 24 24"><path d="M5 3l4 1 1 5-2 2a12 12 0 0 0 5 5l2-2 5 1 1 4-3 2C10 20 4 14 3 6z" fill="none" stroke="#777" stroke-width="1.6"/></svg>0371 / 000 45 60</span>
  <span style="left:985px"><svg width="14" height="10" viewBox="0 0 14 10"><rect x="0.5" y="0.5" width="13" height="9" fill="none" stroke="#777"/><path d="M1 1l6 5 6-5" fill="none" stroke="#777"/></svg>info@frenk-gitterwerk.de</span>
</div>

<div class="abs header">
  <div class="brand"><i></i>Tor &amp; Zaunbau Frenk</div>
  <div class="nav" style="left:694px;font-weight:700;color:var(--ink)">Über uns</div>
  <div class="nav" style="left:861px">Unsere Leistungen</div>
  <div class="nav" style="left:1084px">Kontakt</div>
</div>

<div class="photo" role="img" aria-label="Foto: Holzlattenzaun mit Schiebetor vor Carport und Einfahrt" style="left:0;top:116px;width:1200px;height:476px;background:linear-gradient(180deg,#7d9a62 0%,#9c8a6a 45%,#a9743f 75%,#8b4a1f 100%)"></div>
<div class="abs hero-card">
  <h1>Der rechtige "Rahmen" für Ihr privates oder gewerbliches Grundstück</h1>
  <p>Mehr als 25-Jahre Erfahrung im Tor- und Zaunbau</p>
</div>

<div class="photo" role="img" aria-label="Foto: Metallzaun vor Vorgarten mit Palme und Blumen" style="left:67px;top:685px;width:423px;height:319px;background:linear-gradient(180deg,#d9dde2 0%,#8aa070 55%,#a5a8aa 100%)"></div>
<div class="abs watermark" style="left:540px;top:660px;font-size:92px">FRENK</div>
<div class="abs intro" style="left:542px;top:710px;width:560px">
  <h2>Tor &amp; Zaunbau Frenk aus Chemnitz</h2>
  <p style="font-size:15.5px;line-height:24px;margin-top:18px">Ihr Partner für alle Zaun- und Torsysteme in den Regionen Chemnitz und Zwickau.</p>
  <p class="small" style="margin-top:24px">Wenn es um Zäune, Toranlagen, Schranken geht, ob als Objektschutz für Industrieanlagen, als Lärmschutz für öffentliche Einrichtungen oder ganz einfach als Schmuck und Schutz vor Einblicken im Privatbereich – bei Tor &amp; Zaunbau Frenk können Sie sich auf einen Rund-Um-Service verlassen.</p>
</div>

<div class="abs watermark" style="left:62px;top:1050px;font-size:92px">STÄRKEN</div>
<div class="abs" style="left:64px;top:1105px"><h2>Unsere <b>Stärken</b></h2></div>
<ul class="abs strengths" style="left:67px;top:1147px">
  <li><svg width="16" height="12" viewBox="0 0 16 12"><path d="M1 6l5 5L15 1" fill="none" stroke="#333" stroke-width="2.4"/></svg>Briefkastenanlagen</li>
  <li><svg width="16" height="12" viewBox="0 0 16 12"><path d="M1 6l5 5L15 1" fill="none" stroke="#333" stroke-width="2.4"/></svg>Elektrische Torantriebe</li>
  <li><svg width="16" height="12" viewBox="0 0 16 12"><path d="M1 6l5 5L15 1" fill="none" stroke="#333" stroke-width="2.4"/></svg>Dreh- &amp; Schiebetore</li>
  <li><svg width="16" height="12" viewBox="0 0 16 12"><path d="M1 6l5 5L15 1" fill="none" stroke="#333" stroke-width="2.4"/></svg>Schmuckvolle &amp; zweckmäßige Zäune</li>
  <li><svg width="16" height="12" viewBox="0 0 16 12"><path d="M1 6l5 5L15 1" fill="none" stroke="#333" stroke-width="2.4"/></svg>Schlüsselfertige Erstellung komplexer Toranlagen</li>
</ul>
<div class="photo" role="img" aria-label="Foto: Holzlattenzaun mit Einfahrt vor Einfamilienhaus" style="left:490px;top:1004px;width:643px;height:429px;background:linear-gradient(180deg,#8fb0d6 0%,#d8d2c4 40%,#b06a30 62%,#4d4f52 100%)"></div>

<div class="abs services">
  <div class="photo" role="img" aria-label="Ornamentales Gittermuster im Hintergrund" style="left:800px;top:330px;width:400px;height:348px;background:#eeeeee"></div>
  <div class="abs" style="left:64px;top:57px"><h2>Unsere <b>Leistungen</b></h2></div>
  <p class="abs small" style="left:66px;top:119px;width:1010px">Von der Beratung und Planung über Fertigung und Montage bis hin zu Service und Wartung haben Sie in uns einen direkten Ansprechpartner. Lassen Sie sich auf den folgenden Seiten überraschen und anregen von der Vielfalt der Möglichkeiten und den Beispielen unserer Arbeiten.</p>

  <div class="photo" role="img" aria-label="Foto: Drehflügeltor aus Metall" style="left:67px;top:203px;width:247px;height:137px;background:linear-gradient(180deg,#c9b49c,#6b6b6b)"></div>
  <div class="photo" role="img" aria-label="Foto: Metallzaun am Hang" style="left:340px;top:203px;width:247px;height:137px;background:linear-gradient(180deg,#b6b9bb,#b8552a 55%,#6f8e4d)"></div>
  <div class="photo" role="img" aria-label="Foto: Schiebetor aus Metall" style="left:614px;top:203px;width:248px;height:137px;background:linear-gradient(180deg,#e2c7c6,#3b3d3f 60%,#8e8e8e)"></div>
  <div class="photo" role="img" aria-label="Foto: Holzzaun vor Wohnhaus" style="left:887px;top:203px;width:248px;height:137px;background:linear-gradient(180deg,#9fb9d9,#c07038 55%,#5a5c5f)"></div>

  <div class="abs card-label" style="left:67px;top:355px;width:247px">Drehflügeltore <svg width="22" height="8" viewBox="0 0 22 8"><path d="M0 4h20M16 1l4 3-4 3" fill="none" stroke="#333"/></svg></div>
  <div class="abs card-label" style="left:340px;top:355px;width:247px">Metallzaun <svg width="22" height="8" viewBox="0 0 22 8"><path d="M0 4h20M16 1l4 3-4 3" fill="none" stroke="#333"/></svg></div>
  <div class="abs card-label" style="left:614px;top:355px;width:248px">Schiebetore <svg width="22" height="8" viewBox="0 0 22 8"><path d="M0 4h20M16 1l4 3-4 3" fill="none" stroke="#333"/></svg></div>
  <div class="abs card-label" style="left:887px;top:355px;width:248px">Holzzäune <svg width="22" height="8" viewBox="0 0 22 8"><path d="M0 4h20M16 1l4 3-4 3" fill="none" stroke="#333"/></svg></div>

  <div class="photo" role="img" aria-label="Foto: Sichtschutzzaun aus Holz mit farbigen Pfosten" style="left:67px;top:445px;width:247px;height:119px;background:linear-gradient(180deg,#cfd8df,#a55a28 40%,#8a5a38)"></div>
  <div class="photo" role="img" aria-label="Foto: Hochbeet aus Metall" style="left:340px;top:445px;width:247px;height:119px;background:linear-gradient(180deg,#b9bbb7,#5c6066 60%,#a8a9a6)"></div>
  <div class="photo" role="img" aria-label="Foto: Elektrisches Holztor mit Briefkastenanlage" style="left:614px;top:445px;width:248px;height:119px;background:linear-gradient(180deg,#c4d1e0,#b66c32 50%,#8c5a34)"></div>

  <div class="abs card-label" style="left:67px;top:580px;width:247px">Sichtschutzanlagen <svg width="22" height="8" viewBox="0 0 22 8"><path d="M0 4h20M16 1l4 3-4 3" fill="none" stroke="#333"/></svg></div>
  <div class="abs card-label" style="left:340px;top:580px;width:247px">Gartenaccessoires <svg width="22" height="8" viewBox="0 0 22 8"><path d="M0 4h20M16 1l4 3-4 3" fill="none" stroke="#333"/></svg></div>
  <div class="abs card-label" style="left:614px;top:573px;width:248px;font-size:10px;line-height:14px"><span>Elektrische Torantriebe &amp;<br>Briefkastenanlagen</span> <svg width="22" height="8" viewBox="0 0 22 8"><path d="M0 4h20M16 1l4 3-4 3" fill="none" stroke="#333"/></svg></div>
</div>

<div class="abs" style="left:67px;top:2295px"><h2>Wir suchen <b style="color:var(--accent)">Sie</b></h2></div>
<p class="abs" style="left:67px;top:2355px;width:440px;font-size:16px;line-height:24px">für die Anfertigung und Montage von Tor- und Zaunanlagen in Chemnitz und Umgebung</p>
<p class="abs small" style="left:63px;top:2431px;width:490px">Es erwartet Sie eine abwechslungsreiche und unbefristete Tätigkeit in einem sich ständig ändernden Umfeld. Die Bezahlung erfolgt je nach Eignung und Ausbildung.</p>
<p class="abs small" style="left:63px;top:2526px;width:490px">Für weitere Fragen steht Ihnen Herr Frenk unter 0172 / 000 12 34 zur Verfügung.</p>
<p class="abs small" style="left:63px;top:2599px">Bitte senden Sie Ihre Unterlagen an: <a href="#">info@frenk-gitterwerk.de</a></p>

<div class="abs" style="left:589px;top:2300px;font-size:15px">Ihr <b style="color:var(--accent)">Profil:</b></div>
<div class="abs profile">
  <div class="row"><svg width="52" height="34" viewBox="0 0 52 34"><path d="M8 28a18 18 0 0 1 36 0M4 28h44v3H4zM22 10v-4h8v4" fill="none" stroke="#555" stroke-width="1.6"/></svg><span><b>Ausbildung</b> in einem handwerklichen Beruf</span></div>
  <div class="row"><svg width="52" height="48" viewBox="0 0 52 48"><path d="M10 40L40 8l4 4-30 32zM6 44l6-6" fill="none" stroke="#555" stroke-width="1.6"/></svg><span><b>Fähigkeit und Erfahrung</b> mit den Werkstoffen Holz, Metall, Beton; gern auch Kenntnisse in der Elektrotechnik</span></div>
  <div class="row"><svg width="52" height="50" viewBox="0 0 52 50"><path d="M16 14a10 10 0 0 1 20 0zM12 48c0-12 6-18 14-18s14 6 14 18" fill="none" stroke="#555" stroke-width="1.6"/><circle cx="26" cy="21" r="6" fill="none" stroke="#555" stroke-width="1.6"/></svg><span><b>Körperlich</b> belastbar</span></div>
  <div class="row"><svg width="52" height="34" viewBox="0 0 52 34"><path d="M2 6h30v20H2zM32 12h10l6 7v7H32" fill="none" stroke="#555" stroke-width="1.6"/><circle cx="10" cy="28" r="4" fill="#fff" stroke="#555" stroke-width="1.6"/><circle cx="40" cy="28" r="4" fill="#fff" stroke="#555" stroke-width="1.6"/></svg><span><b>Führerschein</b></span></div>
  <div class="row"><svg width="52" height="50" viewBox="0 0 52 50"><path d="M6 6l40 40M46 6L6 46M10 4l6 6M42 4l-6 6" fill="none" stroke="#555" stroke-width="1.6"/></svg><span><b>Bereitschaft, ständig</b> neues zu lernen</span></div>
</div>

<div class="photo" role="img" aria-label="Foto: Holzhaus mit Carport hinter Holzlattenzaun" style="left:0;top:2851px;width:1056px;height:490px;background:linear-gradient(180deg,#ffffff 0%,#c9d3dc 18%,#3b3e44 40%,#b8762f 65%,#c98a3c 100%)"></div>
<div class="abs" style="left:1114px;top:3302px;transform:rotate(-90deg);transform-origin:0 0;font-size:19px;letter-spacing:1px;color:var(--ink);white-space:nowrap">AUS <b>CHEMNITZ</b></div>

<div class="abs footer">
  <h4 style="left:67px">DU HAST FRAGEN AN UNS?</h4>
  <p style="position:absolute;left:67px;top:73px;font-size:9.5px;line-height:14px">Schreibe uns gerne jederzeit eine E-Mail an:<br>info@frenk-gitterwerk.de</p>
  <h4 style="left:351px">Navigation</h4>
  <ul style="left:351px"><li>Über uns</li><li>Kontakt</li><li>Impressum</li><li>Datenschutz</li></ul>
  <h4 style="left:525px">Leistungen</h4>
  <ul style="left:525px"><li>Drehflügeltore</li><li>Schiebetore</li><li>Sichtschutzanlagen</li><li>Holzzäune</li><li>Metallzaun</li><li>Elektrische Torantriebe &amp; Briefkastenanlagen</li><li>Gartenaccessoires</li></ul>
  <h4 style="left:873px">Kontakt</h4>
  <ul style="left:873px;top:76px"><li><b>Tel.</b>&nbsp;&nbsp; 0371 / 000 45 60</li><li><b>Mobil</b>&nbsp;&nbsp; 0172 / 000 12 34</li><li><b>Fax</b>&nbsp;&nbsp; 0371 / 000 45 61</li></ul>
  <div style="position:absolute;left:67px;top:279px;width:1066px;height:1px;background:#666"></div>
  <p style="position:absolute;left:67px;top:295px;font-size:9.5px">© 2020 Tor &amp; Zaunbau Frenk</p>
</div>

</body>
</html>
```